New Business Card Design Project

We would like a business card that represents the sale of boat, home, auto, and life insurance.

The logo can change colors to meet the look of the design if needed.

Industry/Entity Type

Business

```html
<!DOCTYPE html>
<html lang="en">
<head>
<meta charset="UTF-8">
<title>Halden Financial – Business Card</title>
<link href="https://fonts.googleapis.com/css2?family=Jost:wght@400;500&family=Open+Sans:wght@400;600&display=swap" rel="stylesheet">
<style>
  :root {
    --backdrop: #e4e2df;
    --card-dark: #363636;
    --card-light: #ffffff;
    --ink-light: #ffffff;
    --ink-dark: #2f2f2f;
    --ink-body: #222222;
    --accent-green: #6f9a3a;
    --rule: #1e1e1e;
  }
  * { margin: 0; padding: 0; box-sizing: border-box; }
  html, body {
    width: 1200px; height: 1000px; overflow: hidden;
    background: var(--backdrop);
  }
  .canvas { position: relative; width: 1200px; height: 1000px; }

  .card {
    position: absolute; left: 265px; width: 666px; height: 397px;
    box-shadow: 0 4px 14px rgba(0,0,0,0.18);
  }
  .card--front { top: 73px; background: var(--card-dark); color: var(--ink-light); }
  .card--back  { top: 533px; background: var(--card-light); color: var(--ink-body); }

  .brand-mark { position: absolute; border-radius: 50%; }
  .card--front .brand-mark { left: 298px; top: 72px; width: 70px; height: 70px; background: var(--ink-light); }
  .card--back .brand-mark { left: 133px; top: 28px; width: 58px; height: 58px; background: var(--accent-green); }

  .brand-name {
    position: absolute; text-align: center;
    font-family: 'Jost', sans-serif; font-weight: 400; line-height: 1;
  }
  .brand-name span { display: block; }
  .card--front .brand-name { left: 0; width: 666px; top: 180px; color: var(--ink-light); }
  .card--front .brand-name .line-1 { font-size: 58px; letter-spacing: 10px; padding-left: 10px; }
  .card--front .brand-name .line-2 { font-size: 38px; letter-spacing: 11px; margin-top: 10px; padding-left: 11px; }
  .card--back .brand-name { left: 23px; width: 278px; top: 108px; color: var(--ink-dark); }
  .card--back .brand-name .line-1 { font-size: 45px; letter-spacing: 8px; padding-left: 8px; }
  .card--back .brand-name .line-2 { font-size: 27px; letter-spacing: 8px; margin-top: 6px; padding-left: 8px; }

  .tagline {
    position: absolute; text-align: center;
    font-family: 'Jost', sans-serif; font-weight: 400; line-height: 1;
  }
  .card--front .tagline { left: 0; width: 666px; top: 286px; font-size: 27px; letter-spacing: 2px; }
  .card--back .tagline { left: 23px; width: 278px; top: 192px; font-size: 21px; letter-spacing: 1.5px; color: var(--ink-dark); }

  .card--front .web {
    position: absolute; left: 0; width: 666px; top: 351px; text-align: center;
    font-family: 'Open Sans', sans-serif; font-size: 16px;
  }

  .person { position: absolute; right: 24px; top: 212px; text-align: right; font-family: 'Open Sans', sans-serif; }
  .person__name { font-size: 18px; font-weight: 600; color: var(--accent-green); line-height: 1.2; }
  .person__title { font-size: 15px; color: var(--ink-body); line-height: 1.4; }

  .divider { position: absolute; left: 23px; width: 619px; top: 263px; height: 2px; background: var(--rule); }

  .address {
    position: absolute; left: 23px; top: 293px;
    font-family: 'Open Sans', sans-serif; font-size: 15.5px; line-height: 23px;
  }

  .contacts {
    position: absolute; right: 24px; top: 279px; list-style: none;
    font-family: 'Open Sans', sans-serif; font-size: 15.5px; line-height: 24.5px;
  }
  .contacts li { display: flex; justify-content: flex-end; align-items: center; gap: 6px; }
  .contacts svg { width: 15px; height: 15px; fill: var(--accent-green); }
</style>
</head>
<body>
<div class="canvas">

  <section class="card card--front">
    <div class="brand-mark"></div>
    <div class="brand-name"><span class="line-1">HALDEN</span><span class="line-2">financial</span></div>
    <div class="tagline">investments &amp; insurance</div>
    <div class="web">www.haldenfinancialinvestments.com</div>
  </section>

  <section class="card card--back">
    <div class="brand-mark"></div>
    <div class="brand-name"><span class="line-1">HALDEN</span><span class="line-2">financial</span></div>
    <div class="tagline">investments &amp; insurance</div>

    <div class="person">
      <div class="person__name">DANIEL WHITCOMBE</div>
      <div class="person__title">Managing Director</div>
    </div>

    <div class="divider"></div>

    <address class="address" style="font-style:normal">
      14 Carrow Lane<br>Ashvale VIC 3761
    </address>

    <ul class="contacts">
      <li>+61 3 9400 2185
        <svg viewBox="0 0 16 16" aria-hidden="true"><path d="M2 5c0-2 2-3 6-3s6 1 6 3v1h-3V4.5H5V6H2zM4 7h8l2 6H2z"/><circle cx="8" cy="10" r="1.6" fill="#fff"/></svg>
      </li>
      <li>+61 3 9400 2186
        <svg viewBox="0 0 16 16" aria-hidden="true"><path d="M4 1h7l1 1v3H4zM1 6h14v6h-3v-2H4v2H1zM5 11h6v4H5z"/></svg>
      </li>
      <li>info@haldenfinancial.com
        <svg viewBox="0 0 16 16" aria-hidden="true"><path d="M1 3h14v10H1z"/><path d="M1.5 3.5L8 9l6.5-5.5" stroke="#fff" stroke-width="1.3" fill="none"/></svg>
      </li>
      <li>www.haldenfinancial.com
        <svg viewBox="0 0 16 16" aria-hidden="true"><circle cx="8" cy="8" r="7"/><path d="M1 8h14M8 1v14M8 1c-3 3-3 11 0 14M8 1c3 3 3 11 0 14" stroke="#fff" stroke-width="1" fill="none"/></svg>
      </li>
    </ul>
  </section>

</div>
</body>
</html>
```